business card design for heron textile printing

Heron Textile Printing requires elegant and colorful designs for its business card, ensuring both are visually cohesive and reflect the brand’s creative, modern identity. The logo is already finalized and should be a central element in designs.

## Business Card Design Brief

- Feature the logo clearly, with colors and style matching the letterhead.
- Present contact information (name, title, phone, email, website, address) in a clear, organized manner.
- Open to creative layouts, finishes, and double-sided designs, as long as the card remains professional and easy to read.
- Ensure both pieces feel unified as part of the same brand identity.

The final designs should be vibrant, professional, and memorable, showcasing Heron Textile Printing’s creative spirit.

Target Market(s)

Pakistan

Industry/Entity Type

Textile printing

Other font styles liked:
• Calibri

Requirements
Must have
• Address Email Address Phone number designer can ask me when start designing

```html
<!DOCTYPE html>
<html lang="en">
<head>
<meta charset="UTF-8">
<title>Heron Textile Printing — Business Card</title>
<link rel="stylesheet" href="https://fonts.googleapis.com/css2?family=Montserrat:wght@500;600;700&display=swap">
<style>
  :root {
    --bg: #3a3a3c;
    --card-black: #1a1a1a;
    --white: #ffffff;
    --orange: #f47a1f;
    --pink: #d9357a;
    --maroon: #4a1a1a;
    --cream: #f6efdc;
    --text-light: #f2f2f2;
  }
  * { margin: 0; padding: 0; box-sizing: border-box; }
  html, body {
    width: 1200px; height: 1200px; overflow: hidden;
    background: var(--bg);
    font-family: "Montserrat", "Calibri", sans-serif;
  }
  .canvas {
    width: 1200px; height: 1200px;
    display: flex; flex-direction: column; align-items: center; justify-content: center; gap: 40px;
  }
  .card {
    position: relative;
    width: 960px; height: 548px;
    border-radius: 40px;
    overflow: hidden;
    background: var(--card-black);
    box-shadow: 0 0 0 3px var(--orange), 0 18px 40px rgba(0,0,0,.45);
  }
  .card-art { position: absolute; inset: 0; width: 100%; height: 100%; }

  /* Front */
  .contact {
    position: absolute; left: 92px; top: 210px;
    color: var(--text-light);
  }
  .contact .full-name {
    color: var(--orange); font-weight: 700; font-size: 50px; letter-spacing: 1px; line-height: 1;
  }
  .contact .title {
    font-weight: 500; font-size: 30px; letter-spacing: 1px; margin: 6px 0 22px;
  }
  .contact-list { list-style: none; }
  .contact-list li {
    display: flex; align-items: flex-start; gap: 14px;
    font-size: 22px; font-weight: 500; line-height: 1.2; margin-bottom: 12px;
  }
  .contact-list svg { width: 22px; height: 22px; flex: none; margin-top: 2px; fill: var(--orange); }

  .brand-front {
    position: absolute; left: 560px; top: 200px; width: 340px;
    display: flex; flex-direction: column; align-items: center; gap: 10px;
  }
  .brand-dot { width: 96px; height: 96px; border-radius: 50%; background: var(--orange); margin-bottom: 10px; }
  .brand-name {
    font-weight: 700; font-size: 30px; letter-spacing: 2px; text-align: center; line-height: 1.25;
    text-transform: uppercase;
  }
  .brand-front .brand-name { color: var(--maroon); }

  /* Back */
  .brand-back {
    position: absolute; inset: 0;
    display: flex; flex-direction: column; align-items: center; justify-content: center; gap: 10px;
  }
  .brand-back .brand-dot { width: 150px; height: 150px; }
  .brand-back .brand-name { color: var(--cream); font-size: 40px; }
</style>
</head>
<body>
<main class="canvas">

  <section class="card card-front" aria-label="Business card front">
    <svg class="card-art" viewBox="0 0 960 548" preserveAspectRatio="none" aria-hidden="true">
      <defs>
        <linearGradient id="arcGradient" x1="0" y1="0" x2="1" y2="1">
          <stop offset="0" stop-color="#f47a1f"/>
          <stop offset="1" stop-color="#d9357a"/>
        </linearGradient>
      </defs>
      <path d="M404 0 Q470 470 760 548" fill="none" stroke="url(#arcGradient)" stroke-width="12"/>
      <path d="M424 0 Q490 462 780 548 L960 548 L960 0 Z" fill="#ffffff"/>
    </svg>

    <div class="contact">
      <h1 class="full-name">FULL NAME</h1>
      <p class="title">TITLE</p>
      <ul class="contact-list">
        <li>
          <svg viewBox="0 0 24 24"><path d="M6.6 10.8a15.1 15.1 0 0 0 6.6 6.6l2.2-2.2a1 1 0 0 1 1-.25 11.4 11.4 0 0 0 3.6.57 1 1 0 0 1 1 1V20a1 1 0 0 1-1 1A17 17 0 0 1 3 4a1 1 0 0 1 1-1h3.5a1 1 0 0 1 1 1c0 1.25.2 2.45.57 3.57a1 1 0 0 1-.25 1z"/></svg>
          <span>(000) 000 0000</span>
        </li>
        <li>
          <svg viewBox="0 0 24 24"><path d="M2 5h20v14H2z M3 6l9 7 9-7" fill="none" stroke="#f47a1f" stroke-width="2"/></svg>
          <span>email@company.com</span>
        </li>
        <li>
          <svg viewBox="0 0 24 24"><path d="M12 2a7 7 0 0 0-7 7c0 5 7 13 7 13s7-8 7-13a7 7 0 0 0-7-7zm0 9.5A2.5 2.5 0 1 1 12 6.5a2.5 2.5 0 0 1 0 5z"/></svg>
          <span>123 Name Street, 000<br>Your City, 00000-000</span>
        </li>
      </ul>
    </div>

    <div class="brand-front">
      <span class="brand-dot" aria-hidden="true"></span>
      <p class="brand-name">Heron Textile Printing</p>
    </div>
  </section>

  <section class="card card-back" aria-label="Business card back">
    <div class="brand-back">
      <span class="brand-dot" aria-hidden="true"></span>
      <p class="brand-name">Heron Textile Printing</p>
    </div>
  </section>

</main>
</body>
</html>
```